Professional Services (B-2-B) Business Cards (Front & Back)

Quintarion is a business-to-business professional services company in the legal sector. They typically present to c-suite and executive functions who are looking for providers with expertise, and experience. Our business card should look and feel professional and contemporary, but we are not a startup tech company, so we want the tone to be more mature.

```html
<!DOCTYPE html>
<html lang="en">
<head>
<meta charset="utf-8">
<title>Quintarion Business Cards</title>
<link href="https://fonts.googleapis.com/css2?family=Montserrat:wght@400;500;700&display=swap" rel="stylesheet">
<style>
  :root {
    --navy: #1c2b63;
    --navy-deep: #17244f;
    --paper: #f3f4f6;
    --ink-light: #e9ebf2;
    --backdrop: #dfe3e6;
  }
  html, body {
    margin: 0;
    padding: 0;
    width: 1200px;
    height: 900px;
    overflow: hidden;
    background: var(--backdrop);
    font-family: "Montserrat", sans-serif;
  }
  .canvas {
    position: relative;
    width: 1200px;
    height: 900px;
  }
  .card {
    position: absolute;
    left: 320px;
    width: 560px;
    height: 320px;
    background: var(--navy);
    color: var(--ink-light);
    overflow: hidden;
    box-shadow: 0 10px 28px rgba(20, 30, 60, 0.22);
  }
  .card-front { top: 100px; }
  .card-back { top: 480px; background: linear-gradient(160deg, var(--navy) 0%, var(--navy-deep) 100%); }

  /* Wordmark */
  .wordmark {
    position: absolute;
    display: flex;
    align-items: center;
    gap: 14px;
  }
  .wordmark-square {
    width: 22px;
    height: 22px;
    background: var(--paper);
  }
  .wordmark-name {
    font-weight: 500;
    letter-spacing: 0.42em;
    color: var(--paper);
    text-transform: uppercase;
  }
  .card-front .wordmark { left: 30px; top: 96px; }
  .card-front .wordmark-name { font-size: 17px; }

  /* Front: name block */
  .person {
    position: absolute;
    right: 40px;
    top: 34px;
    text-align: right;
  }
  .person-name {
    font-weight: 700;
    font-size: 24px;
    color: var(--paper);
    line-height: 1.1;
  }
  .person-title {
    font-weight: 500;
    font-size: 13px;
    line-height: 1.4;
  }
  .person-marker {
    position: absolute;
    right: 14px;
    top: 30px;
    width: 10px;
    height: 36px;
    background: var(--paper);
  }

  /* Front: contact block */
  .contact {
    position: absolute;
    left: 60px;
    top: 150px;
    font-size: 12.5px;
    line-height: 1.4;
  }
  .contact-address { margin: 0 0 8px; }
  .contact-list { list-style: none; margin: 0; padding: 0; }
  .contact-list li { display: flex; align-items: center; gap: 8px; }
  .contact-icon { width: 10px; height: 10px; flex: none; }

  /* Front: bottom rule */
  .rule-thin {
    position: absolute;
    left: 0;
    bottom: 28px;
    width: 380px;
    height: 3px;
    background: var(--paper);
  }
  .rule-thin-end {
    position: absolute;
    right: 0;
    bottom: 28px;
    width: 22px;
    height: 3px;
    background: var(--paper);
  }
  .band-bottom {
    position: absolute;
    left: 0;
    right: 0;
    bottom: 0;
    height: 14px;
    background: var(--paper);
  }
  .card-front .site {
    position: absolute;
    right: 30px;
    bottom: 22px;
    font-size: 13px;
    font-weight: 400;
  }
  .site strong { font-weight: 700; }

  /* Back */
  .card-back .wordmark {
    left: 50%;
    top: 118px;
    transform: translateX(-50%);
    gap: 20px;
  }
  .card-back .wordmark-square { width: 30px; height: 30px; }
  .card-back .wordmark-name { font-size: 22px; }
  .back-footer {
    position: absolute;
    left: 40px;
    right: 40px;
    top: 218px;
    display: flex;
    align-items: center;
    gap: 16px;
  }
  .back-line {
    flex: 1;
    height: 1.5px;
    background: linear-gradient(90deg, rgba(233,235,242,0) 0%, var(--ink-light) 100%);
  }
  .back-line.right {
    background: linear-gradient(90deg, var(--ink-light) 0%, rgba(233,235,242,0) 100%);
  }
  .back-footer .site { font-size: 14px; }
</style>
</head>
<body>
<main class="canvas">

  <section class="card card-front" aria-label="Business card front">
    <span class="person-marker"></span>
    <div class="person">
      <div class="person-name">Mark Halden</div>
      <div class="person-title">President &amp; CEO</div>
    </div>

    <div class="wordmark">
      <span class="wordmark-square"></span>
      <span class="wordmark-name">Quintarion</span>
    </div>

    <div class="contact">
      <p class="contact-address">4280 Harbor Blvd<br>Suite 210<br>Eastfield, IN-46201</p>
      <ul class="contact-list">
        <li>
          <svg class="contact-icon" viewBox="0 0 10 10" aria-hidden="true"><path d="M2 0.5 L3.6 0.5 L4.2 2.8 L3 3.6 Q4 5.8 6.4 7 L7.2 5.8 L9.5 6.4 L9.5 8 Q9.5 9.5 8 9.5 Q1 8.5 0.5 2 Q0.5 0.5 2 0.5 Z" fill="#f3f4f6"/></svg>
          (555) 318 – 2760
        </li>
        <li>
          <svg class="contact-icon" viewBox="0 0 10 10" aria-hidden="true"><path d="M2 0.5 L3.6 0.5 L4.2 2.8 L3 3.6 Q4 5.8 6.4 7 L7.2 5.8 L9.5 6.4 L9.5 8 Q9.5 9.5 8 9.5 Q1 8.5 0.5 2 Q0.5 0.5 2 0.5 Z" fill="#f3f4f6"/></svg>
          (555) 647 – 1093
        </li>
        <li>
          <svg class="contact-icon" viewBox="0 0 10 10" aria-hidden="true"><rect x="0.5" y="2" width="9" height="6.5" fill="#f3f4f6"/><path d="M0.5 2 L5 5.6 L9.5 2" fill="none" stroke="#1c2b63" stroke-width="1"/></svg>
          mhalden@quintarion.tech
        </li>
      </ul>
    </div>

    <span class="rule-thin"></span>
    <div class="site">www.<strong>quintarion</strong>.tech</div>
    <span class="rule-thin-end"></span>
    <span class="band-bottom"></span>
  </section>

  <section class="card card-back" aria-label="Business card back">
    <div class="wordmark">
      <span class="wordmark-square"></span>
      <span class="wordmark-name">Quintarion</span>
    </div>
    <div class="back-footer">
      <span class="back-line"></span>
      <span class="site">www.quintarion.tech</span>
      <span class="back-line right"></span>
    </div>
  </section>

</main>
</body>
</html>
```